LUMINARA VENTURES NAMECARD

Need to design a name card with an existing logo.

As we are professional corporate services provider our name card has to project a professional image.
Should be corporate, simple & professional.

Our corporate color is maroon red but not too dull.

Please refer to our website at www.luminaraventures.com.sg

Would attach our logo herewith.

Front surface of namecard details:
LUMINARA VENTURES PTE LTD
Registration No. 208711845K

Tan Wei Ling CA (Singapore)
Director

Tel +65 6481 2957
Mobile +65 9172 3086
tan@luminaraventures.com.sg
www.luminaraventures.com.sg

47 Plover Lane
#07-12 Harbourlight Plaza
Singapore 276351

Back of namecard:-
OUR CORE SERVICES
Incorporation services
Corporate Secretarial Services
Accountancy service
Goods & Services Taxation
Corporate & Personal Taxation
Financial Reporting
Payroll Administration

AFFILIATES:
BRIGHTWAVE CORPORATE SERVICES PTE LTD
PINNACLEFORMATIONSPTE LTD
LIM MANAGEMENT SERVICES PTE LTD
RW HO AND COMPANY PTE LTD
LEDGERLY ACADEMY

```html
<!DOCTYPE html>
<html lang="en">
<head>
<meta charset="utf-8">
<title>Luminara Ventures Namecard</title>
<link rel="stylesheet" href="https://fonts.googleapis.com/css2?family=Source+Sans+3:wght@400;600;700&display=swap">
<style>
  :root {
    --canvas: #2b2b2d;
    --maroon-light: #e2263f;
    --maroon: #c21a31;
    --maroon-deep: #a8142a;
    --paper: #f7f7f6;
    --ink: #3d3d3f;
    --ink-soft: #6b6b6e;
    --rule: #9a9a9c;
    --white: #ffffff;
  }
  * { box-sizing: border-box; margin: 0; padding: 0; }
  html, body {
    width: 1200px; height: 900px; overflow: hidden;
    background: var(--canvas);
    font-family: "Source Sans 3", "Myriad Pro", Arial, sans-serif;
  }
  .canvas { position: relative; width: 1200px; height: 900px; }
  .card {
    position: absolute; left: 290px; width: 620px; height: 372px;
    overflow: hidden;
  }

  /* Back of card */
  .card--back {
    top: 58px;
    padding: 30px 30px 0;
    background: linear-gradient(135deg, var(--maroon-light) 0%, var(--maroon) 55%, var(--maroon-deep) 100%);
    color: var(--white);
    text-align: center;
    display: flex; flex-direction: column; align-items: center;
  }
  .brand-name--back {
    font-size: 36px; font-weight: 600; letter-spacing: 2px; line-height: 1;
    margin-bottom: 16px;
  }
  .section-title {
    font-size: 17px; font-weight: 700; line-height: 22px;
  }
  .fade-rule {
    width: 460px; height: 1px; flex: none;
    margin: 7px 0;
    background: linear-gradient(90deg, rgba(255,255,255,0), rgba(255,255,255,.85) 50%, rgba(255,255,255,0));
  }
  .list-block {
    font-size: 15.5px; line-height: 21px;
  }
  .list-block span { margin: 0 7px; white-space: nowrap; }

  /* Front of card */
  .card--front {
    top: 470px;
    background: var(--paper);
    color: var(--ink);
  }
  .corner-tab {
    position: absolute; top: 0; right: 0; width: 14px; height: 34px;
    background: var(--maroon);
  }
  .person { position: absolute; top: 26px; right: 34px; text-align: right; }
  .person-name { font-size: 19px; font-weight: 700; color: var(--maroon); }
  .person-role { font-size: 14px; color: var(--ink-soft); }
  .rule { position: absolute; height: 1px; background: var(--rule); }
  .rule--company { top: 148px; left: 300px; right: 34px; }
  .rule--brand { top: 286px; left: 34px; width: 300px; }
  .company {
    position: absolute; top: 160px; right: 34px; text-align: right;
    font-style: normal;
    font-size: 14.5px; line-height: 19px; color: var(--ink-soft);
  }
  .company-name { font-weight: 700; color: var(--maroon); }
  .brand-name--front {
    position: absolute; top: 196px; left: 34px;
    font-size: 40px; font-weight: 600; letter-spacing: 1px; line-height: 1.05;
    color: var(--maroon);
  }
  .contacts {
    position: absolute; top: 294px; left: 34px; list-style: none;
    font-size: 14.5px; line-height: 17px; color: var(--ink);
  }
  .contacts li { display: flex; align-items: center; gap: 8px; }
  .contacts svg { width: 12px; height: 12px; fill: var(--maroon); flex: none; }
</style>
</head>
<body>
<main class="canvas">

  <section class="card card--back" aria-label="Back of namecard">
    <div class="brand-name brand-name--back">LUMINARA<br>VENTURES</div>
    <h2 class="section-title">Our Core Services</h2>
    <div class="fade-rule"></div>
    <p class="list-block">
      <span>Incorporation services</span><span>Corporate Secretarial Services</span><br>
      <span>Accountancy service</span><span>Goods &amp; Services Taxation</span><br>
      <span>Corporate &amp; Personal Taxation</span><span>Financial Reporting</span><br>
      <span>Payroll Administration</span>
    </p>
    <div class="fade-rule"></div>
    <h2 class="section-title">Affiliates</h2>
    <div class="fade-rule"></div>
    <p class="list-block">
      <span>Brightwave Corporate Services PTE Ltd</span><span>Pinnacleformations PTE LTD</span><br>
      <span>Lim Management Services PTE LTD</span><span>RW Ho and company PTE LTD</span><span>Ledgerly Academy</span>
    </p>
  </section>

  <section class="card card--front" aria-label="Front of namecard">
    <div class="corner-tab"></div>
    <div class="person">
      <div class="person-name">Tan Wei Ling CA</div>
      <div class="person-role">Director</div>
    </div>
    <div class="rule rule--company"></div>
    <address class="company">
      <div class="company-name">Luminara Ventures PTE LTD</div>
      <div>47 Plover Lane</div>
      <div>#07-12 Harbourlight Plaza</div>
      <div>Singapore 276351</div>
      <div>Registration No. 208711845K</div>
    </address>
    <div class="brand-name brand-name--front">LUMINARA<br>VENTURES</div>
    <div class="rule rule--brand"></div>
    <ul class="contacts">
      <li><svg viewBox="0 0 12 12" aria-hidden="true"><path d="M1 3.5C1 2 2.5 1 6 1s5 1 5 2.5V5H8.5V4h-5v1H1z M2.5 6h7l1 5h-9z"/></svg>+65 6481 2957</li>
      <li><svg viewBox="0 0 12 12" aria-hidden="true"><path d="M3 0h6v12H3z M4 1.5v7.5h4V1.5z" fill-rule="evenodd"/></svg>+65 9172 3086</li>
      <li><svg viewBox="0 0 12 12" aria-hidden="true"><path d="M0 2h12v8H0z M1 3l5 3.5L11 3v-.2L6 5.8 1 2.8z" fill-rule="evenodd"/></svg>tan@luminaraventures.com.sg</li>
      <li><svg viewBox="0 0 12 12" aria-hidden="true"><circle cx="6" cy="6" r="6"/><path d="M2 6h8M6 1.5v9" stroke="#f7f7f6" stroke-width="1"/></svg>www.luminaraventures.com.sg</li>
    </ul>
  </section>

</main>
</body>
</html>
```